BROTH Nutrition Mobile Application Layout

I am looking for professional grade app page layouts to use in my clickable prototype for an investor pitch.

B.R.O.T.H. is an acronym for Balanced Routine Optimising Tailored Health.

This app is a nutrition diet generation tool for the consumer (type in profile, diet is generated).

I am most interested in several pages consisting of:
- A landing/login page
- User profile page which will consist of a visual representation of adherence to the diet such as a pie chart, bar with percentage representing said adherence, etc.
- Profile settings page
- Blank general layout page (a standard template to be used with all pages in the application)

I would prefer greens, reds, and yellows in the design
The design should reflect health and nutrition
The design should have an "ease of use appearance"

Apps that are useful to look at are:
Vitaltrack Buddy
Macroscope
Quickbasket

I have uploaded a "working" logo that I am using

I look forward to seeing your talents and appreciate your work in advance!

Target Market(s)

General population - health and wellness companies

Industry/Entity Type

Health And Wellness

Font styles to use
Serif
Sans Serif
Other font styles liked:
• Dealer's Choice

Colors
9ccb3b
f04a51
fbed22

Requirements
Must have
• - A landing/login page
• - User profile page which will consist of a visual representation of adherence to the diet such as a pie chart, bar with percentage representing said adherence, etc.
• - Profile settings page
• - Blank general layout page (a standard template to be used with all pages in the application)
• The design should reflect health and nutrition
• The design should have an "ease of use appearance"
Nice to have
• Incorporating the acronym spelled out.
• Common image in the background reflecting nutrition and health.

```html
<!DOCTYPE html>
<html lang="en">
<head>
<meta charset="utf-8">
<title>BROTH – Your Profile</title>
<link rel="stylesheet" href="https://fonts.googleapis.com/css2?family=Nunito+Sans:wght@400;600;700;800&display=swap">
<style>
:root{
  --green:#84c91f;
  --green-dark:#6fb816;
  --yellow:#f8b71c;
  --orange:#f26a2c;
  --red:#e5452a;
  --ink:#222428;
  --text:#3a3c40;
  --muted:#8d9096;
  --track:#eeeff1;
  --band:#eef0f3;
  --line:#e3e4e7;
  --white:#ffffff;
}
*{margin:0;padding:0;box-sizing:border-box}
html,body{width:675px;height:1200px;overflow:hidden;background:var(--white)}
body{font-family:"Nunito Sans",sans-serif;color:var(--ink);position:relative}
.screen{position:relative;width:675px;height:1200px;overflow:hidden}
.header-band{position:absolute;left:0;top:0;width:675px;height:240px}
.status-bar{position:absolute;top:0;left:0;width:675px;height:40px;display:flex;align-items:center;justify-content:space-between;padding:0 12px;font-size:22px;font-weight:600;color:var(--ink)}
.status-left,.status-right{display:flex;align-items:center;gap:8px;width:220px}
.status-right{justify-content:flex-end}
.status-time{position:absolute;left:0;right:0;text-align:center;pointer-events:none}
.signal{display:flex;gap:3px}
.signal span{width:9px;height:9px;border-radius:50%;background:var(--ink)}
.menu-btn{position:absolute;left:22px;top:58px;width:42px;height:30px}
.page-title{position:absolute;top:56px;left:0;width:675px;text-align:center;font-size:27px;font-weight:700;color:#4a4c50}
.avatar{position:absolute;left:243px;top:117px;width:188px;height:188px;border-radius:50%;background:var(--white);padding:9px}
.avatar-photo{width:100%;height:100%;border-radius:50%;background:radial-gradient(circle at 50% 40%,#c9a48a 0%,#8a7468 45%,#3b4450 100%)}
.actions{position:absolute;top:346px;left:18px;width:639px;display:flex;justify-content:space-between}
.action{height:70px;border-radius:35px;color:var(--white);font-size:18px;font-weight:700;letter-spacing:1.5px;display:flex;align-items:center;justify-content:center;text-transform:uppercase}
.action--order{width:202px;background:var(--green)}
.action--change{width:205px;background:var(--yellow)}
.action--activity{width:205px;background:var(--orange)}
.stats{position:absolute;top:486px;left:0;width:675px}
.stat{position:absolute;width:210px;text-align:center}
.stat svg{display:block;margin:0 auto}
.stat-value{position:absolute;top:0;left:0;width:210px;height:180px;display:flex;flex-direction:column;align-items:center;justify-content:center}
.stat-number{font-size:34px;font-weight:700;color:var(--green);line-height:1}
.stat-sub{font-size:16px;font-weight:600;color:var(--text);letter-spacing:1px;margin-top:4px}
.stat-breakdown{font-size:16px;font-weight:800;color:var(--text);line-height:1.3}
.stat-label{margin-top:8px;font-size:22px;font-weight:600;letter-spacing:2px;line-height:1.25;color:var(--ink);text-transform:uppercase}
.pager{position:absolute;top:748px;left:0;width:675px;display:flex;justify-content:center;gap:11px}
.pager span{width:16px;height:16px;border-radius:50%;background:#dcdde0}
.pager span.is-active{background:#b6b8bc}
.divider{position:absolute;left:0;top:797px;width:675px;height:2px;background:var(--line)}
.section-title{position:absolute;left:24px;top:826px;font-size:36px;font-weight:800;letter-spacing:1px;color:#33353a}
.food-list{position:absolute;top:882px;left:0;width:675px;list-style:none}
.food{position:relative;height:117px;border-bottom:2px solid var(--line);margin:0 0 0 24px;padding-right:22px}
.food-icon{position:absolute;left:0;top:24px;width:44px;height:50px}
.food-name{position:absolute;left:73px;top:16px;font-size:27px;font-weight:600;color:var(--ink)}
.food-macros{position:absolute;left:73px;top:62px;font-size:16px;color:var(--muted);letter-spacing:1.5px;display:flex;gap:24px}
.food-macros b{color:var(--text);font-weight:600;font-size:18px;letter-spacing:0}
.food-kcal{position:absolute;right:22px;top:30px;font-size:23px;font-weight:800}
.food-kcal--high{color:var(--red)}
.food-kcal--ok{color:var(--green-dark)}
</style>
</head>
<body>
<main class="screen">
  <svg class="header-band" viewBox="0 0 675 240" aria-hidden="true">
    <path d="M0 0H675V236C560 214 450 206 337 206S115 214 0 236Z" fill="var(--band)"/>
  </svg>

  <div class="status-bar">
    <div class="status-left">
      <div class="signal"><span></span><span></span><span></span><span></span><span></span></div>
      <span>Nimbus</span>
      <svg width="22" height="16" viewBox="0 0 22 16" aria-hidden="true"><path d="M11 15 1 5a14 14 0 0 1 20 0Z" fill="var(--ink)"/></svg>
    </div>
    <div class="status-time">9:41 AM</div>
    <div class="status-right">
      <svg width="14" height="22" viewBox="0 0 14 22" aria-hidden="true"><path d="M2 6l10 10-5 5V1l5 5L2 16" fill="none" stroke="var(--ink)" stroke-width="2" stroke-linejoin="round"/></svg>
      <span>100%</span>
      <svg width="44" height="20" viewBox="0 0 44 20" aria-hidden="true"><rect x="1" y="1" width="38" height="18" rx="4" fill="none" stroke="var(--ink)" stroke-width="2"/><rect x="4" y="4" width="32" height="12" rx="2" fill="var(--ink)"/><rect x="40" y="7" width="3" height="6" rx="1" fill="var(--ink)"/></svg>
    </div>
  </div>

  <svg class="menu-btn" viewBox="0 0 42 30" aria-label="Menu"><g stroke="var(--green)" stroke-width="4" stroke-linecap="round"><line x1="2" y1="3" x2="40" y2="3"/><line x1="2" y1="15" x2="40" y2="15"/><line x1="2" y1="27" x2="40" y2="27"/></g></svg>
  <h1 class="page-title">Your Profile</h1>

  <div class="avatar"><div class="avatar-photo" role="img" aria-label="Profile photo of the user"></div></div>

  <nav class="actions">
    <div class="action action--order">Order Food</div>
    <div class="action action--change">Change Food</div>
    <div class="action action--activity">Daily Activity</div>
  </nav>

  <section class="stats">
    <div class="stat" style="left:12px">
      <svg width="180" height="180" viewBox="0 0 180 180">
        <defs><linearGradient id="calGrad" x1="0" y1="0" x2="0" y2="1"><stop offset="0" stop-color="var(--orange)"/><stop offset="1" stop-color="var(--yellow)"/></linearGradient></defs>
        <circle cx="90" cy="90" r="81" fill="none" stroke="var(--track)" stroke-width="11"/>
        <circle cx="90" cy="90" r="81" fill="none" stroke="url(#calGrad)" stroke-width="11" stroke-linecap="round" stroke-dasharray="422 509" transform="rotate(-90 90 90)"/>
      </svg>
      <div class="stat-value"><span class="stat-number">1250</span><span class="stat-sub">OF 1500</span></div>
      <div class="stat-label">Calories<br>Eaten</div>
    </div>
    <div class="stat" style="left:219px">
      <svg width="180" height="180" viewBox="0 0 180 180">
        <defs><linearGradient id="tgtGrad" x1="0" y1="0" x2="0" y2="1"><stop offset="0" stop-color="var(--green)"/><stop offset="1" stop-color="#b9d81e"/></linearGradient></defs>
        <circle cx="90" cy="90" r="81" fill="none" stroke="var(--track)" stroke-width="11"/>
        <circle cx="90" cy="90" r="81" fill="none" stroke="url(#tgtGrad)" stroke-width="11" stroke-linecap="round" stroke-dasharray="305 509" transform="rotate(-90 90 90)"/>
      </svg>
      <div class="stat-value"><span class="stat-number">60%</span></div>
      <div class="stat-label">Targets<br>Completed</div>
    </div>
    <div class="stat" style="left:440px">
      <svg width="180" height="180" viewBox="0 0 180 180">
        <g fill="none" stroke-width="11" transform="rotate(-90 90 90)">
          <circle cx="90" cy="90" r="81" stroke="var(--orange)" stroke-dasharray="203.6 509"/>
          <circle cx="90" cy="90" r="81" stroke="var(--green)" stroke-dasharray="152.7 509" stroke-dashoffset="-203.6"/>
          <circle cx="90" cy="90" r="81" stroke="#f7d41e" stroke-dasharray="152.7 509" stroke-dashoffset="-356.3"/>
        </g>
      </svg>
      <div class="stat-value"><div class="stat-breakdown">40% CARBS<br>30% FATS<br>30% PROTEINS</div></div>
      <div class="stat-label">Diet<br>Breakdown</div>
    </div>
  </section>

  <div class="pager"><span class="is-active"></span><span></span><span></span></div>
  <div class="divider"></div>

  <h2 class="section-title">TODAY</h2>
  <ul class="food-list">
    <li class="food">
      <svg class="food-icon" viewBox="0 0 44 50" aria-hidden="true"><ellipse cx="22" cy="25" rx="12" ry="20" transform="rotate(35 22 25)" fill="none" stroke="var(--orange)" stroke-width="3"/><circle cx="18" cy="22" r="1.8" fill="var(--orange)"/><circle cx="25" cy="29" r="1.8" fill="var(--orange)"/></svg>
      <span class="food-name">Portion of Sweet Potato Fries</span>
      <div class="food-macros"><span>CARBS <b>27g</b></span><span>FATS <b>2g</b></span><span>PROTEINS <b>5g</b></span></div>
      <span class="food-kcal food-kcal--high">214 kCal</span>
    </li>
    <li class="food">
      <svg class="food-icon" viewBox="0 0 44 50" aria-hidden="true"><g fill="none" stroke="var(--green)" stroke-width="3" stroke-linejoin="round"><path d="M8 24a8 8 0 0 1 4-14 9 9 0 0 1 16-2 8 8 0 0 1 10 8 7 7 0 0 1-4 12H10a6 6 0 0 1-2-4Z"/><path d="M17 28l-2 16h14l-2-16M22 28v10"/></g></svg>
      <span class="food-name">1 Cup of Broccoli</span>
      <div class="food-macros"><span>CARBS <b>27g</b></span><span>FATS <b>2g</b></span><span>PROTEINS <b>5g</b></span></div>
      <span class="food-kcal food-kcal--ok">62 kCal</span>
    </li>
    <li class="food">
      <svg class="food-icon" viewBox="0 0 44 50" aria-hidden="true"><g fill="none" stroke="var(--yellow)" stroke-width="3" stroke-linejoin="round"><rect x="16" y="4" width="12" height="8" rx="2"/><path d="M16 12l-4 8v26h20V20l-4-8Z"/></g></svg>
      <span class="food-name">50g Grated Cheddar Cheese</span>
      <div class="food-macros"><span>CARBS <b>27g</b></span><span>FATS <b>2g</b></span><span>PROTEINS <b>5g</b></span></div>
      <span class="food-kcal food-kcal--ok">102 kCal</span>
    </li>
  </ul>
</main>
</body>
</html>
```